Business card

We are looking for a creative person to deigns our company business card.

Target Market(s)

College age student

Industry/Entity Type

Accommodation

Contact Information for Business Card

We want a fun, clean and sophisticated design. It should look good, but more importantly the information should be legible.

Font styles to use
Serif
Sans Serif
Other font styles liked:
• Open Sans ,

Colors
33a6d7

Requirements
Must have
• Must have a young and memorable message. Be legible.
• Our logo on the back on a solid blue , please find color and logo attached
• LodgeBridgely.net on the back.
Nice to have
• I would like to have couple of different fonts on the LodgeBridgely.net on the back of the cards with a solid blue.

```html
<!DOCTYPE html>
<html lang="en">
<head>
<meta charset="utf-8">
<title>LodgeBridgely business card</title>
<link rel="stylesheet" href="https://fonts.googleapis.com/css2?family=Open+Sans:wght@400;600;700&display=swap">
<style>
  :root {
    --stage: #e9eaec;
    --navy: #0f5d92;
    --navy-deep: #0b558a;
    --sky: #35a0de;
    --paper: #f2f3f5;
    --white: #ffffff;
  }
  * { margin: 0; padding: 0; box-sizing: border-box; }
  html, body {
    width: 1200px; height: 911px; overflow: hidden;
    background: var(--stage);
    font-family: "Open Sans", Arial, sans-serif;
  }
  .stage { position: relative; width: 1200px; height: 911px; }
  .card {
    position: absolute; top: 95px; width: 410px; height: 720px;
    overflow: hidden; box-shadow: 0 10px 30px rgba(0,0,0,.18);
  }
  .card-front { left: 150px; }
  .card-back { left: 640px; background: var(--navy-deep); }
  .front-shapes { position: absolute; inset: 0; }
  .holder {
    position: absolute; left: 30px; top: 38px; color: var(--white);
  }
  .holder-name { font-weight: 700; font-size: 22px; letter-spacing: .5px; }
  .holder-role { font-size: 15px; margin-top: 2px; letter-spacing: .3px; }
  .brand {
    position: absolute; left: 170px; top: 350px;
    display: flex; align-items: center; gap: 8px;
  }
  .brand-mark { width: 14px; height: 14px; background: var(--navy); }
  .brand-name { font-weight: 700; font-size: 25px; color: var(--navy); }
  .contact {
    position: absolute; left: 28px; top: 512px;
    color: var(--white); font-size: 15px; line-height: 21px;
    list-style: none;
  }
  .contact li { display: flex; align-items: center; gap: 8px; white-space: nowrap; }
  .contact .address { padding-left: 22px; }
  .contact svg { width: 14px; height: 14px; flex: none; }
  .back-name {
    position: absolute; left: 50%; top: 50%;
    transform: translate(-50%, -50%) rotate(90deg);
    color: var(--white); font-weight: 700; font-size: 46px;
    white-space: nowrap; letter-spacing: .5px;
  }
</style>
</head>
<body>
<main class="stage">
  <section class="card card-front" aria-label="Card front">
    <svg class="front-shapes" viewBox="0 0 410 720" width="410" height="720" aria-hidden="true">
      <polygon points="0,0 410,0 410,190 0,290" fill="var(--navy)"/>
      <polygon points="0,290 130,263 410,720 0,720" fill="var(--sky)"/>
      <polygon points="130,263 410,190 410,720" fill="var(--paper)"/>
    </svg>
    <div class="holder">
      <p class="holder-name">DANA WHITFIELD</p>
      <p class="holder-role">CEO/FOUNDER</p>
    </div>
    <div class="brand">
      <span class="brand-mark"></span>
      <span class="brand-name">LodgeBridgely</span>
    </div>
    <ul class="contact">
      <li class="address">118 Marlow St, Suite 302</li>
      <li class="address">Fairview, California CA 90417</li>
      <li><svg viewBox="0 0 14 14"><path d="M3 1l3 3-1.5 1.5a8 8 0 0 0 3.5 3.5L9.5 7.5l3 3L11 13C6 12.5 1.5 8 1 3z" fill="#fff"/></svg>555 210 4471</li>
      <li><svg viewBox="0 0 14 14"><rect x="3.5" y="1" width="7" height="12" rx="1.5" fill="none" stroke="#fff" stroke-width="1.5"/></svg>555 318 6092</li>
      <li><svg viewBox="0 0 14 14"><rect x="1" y="5" width="12" height="7" rx="1" fill="#fff"/><rect x="3.5" y="1.5" width="7" height="4" fill="none" stroke="#fff" stroke-width="1.3"/></svg>555 427 8835</li>
      <li><svg viewBox="0 0 14 14"><rect x="1" y="3" width="12" height="8" rx="1" fill="#fff"/><path d="M1.5 3.5L7 8l5.5-4.5" fill="none" stroke="var(--sky)" stroke-width="1.2"/></svg>dana@LodgeBridgely.net</li>
      <li><svg viewBox="0 0 14 14"><circle cx="7" cy="7" r="6" fill="#fff"/><path d="M1 7h12M7 1c-3 3-3 9 0 12M7 1c3 3 3 9 0 12" fill="none" stroke="var(--sky)" stroke-width="1"/></svg>www.LodgeBridgely.net</li>
    </ul>
  </section>

  <section class="card card-back" aria-label="Card back">
    <p class="back-name">LodgeBridgely</p>
  </section>
</main>
</body>
</html>
```